Quorvane Capital Modern Business Card

We need a modern business card template designed for Quorvane Capital.
Quorvane Capital is a diversified global cryptocurrency investment fund.

The font under the logo: Hiragino Kaku Gothic Pro

Color Hexcode: Main colors white (ffffff) & teal (188383), we are open to adding #fcca46 as an accent

Target Market(s)

Accredited Investors, high net worth individuals and institutional investors

Industry/Entity Type

Investment

Contact Information for Business Card

Contact Information should contain
Name
main phone +1 720 555 0147
cell
email

Font styles to use
Sans Serif
Other font styles liked:
• Hiragino Kaku Gothic Pro

Requirements
Must have
• would like to have icons that identify the contact information
• include our website: www.quorvanecapital.example
• include our Tagline: Diversified Crypto Investment Funds
Nice to have
• Would like to have a simple back side with the logo (without the words) and plenty of space

```html
<!DOCTYPE html>
<html lang="en">
<head>
<meta charset="utf-8">
<title>Quorvane Capital – Business Card</title>
<link rel="stylesheet" href="https://fonts.googleapis.com/css2?family=Roboto:wght@400;500&family=Exo+2:wght@500&display=swap">
<style>
  :root {
    --teal: #188383;
    --teal-dark: #147474;
    --gold: #fcca46;
    --white: #ffffff;
    --paper-light: #f5f5f5;
    --paper-dark: #e4e4e4;
    --ink: #1c1c1c;
    --stage: #bcbcbc;
  }
  * { margin: 0; padding: 0; box-sizing: border-box; }
  html, body {
    width: 1200px;
    height: 576px;
    overflow: hidden;
    background: var(--stage);
    font-family: "Roboto", Arial, sans-serif;
  }
  .canvas {
    position: relative;
    width: 1200px;
    height: 576px;
  }
  .card {
    position: absolute;
    top: 138px;
    height: 294px;
    border-radius: 13px;
    overflow: hidden;
  }
  /* Front side */
  .card-front {
    left: 82px;
    width: 484px;
    background: linear-gradient(180deg, var(--teal) 0%, var(--teal-dark) 100%);
  }
  .front-name {
    position: absolute;
    left: 81px;
    top: 116px;
    font-size: 35px;
    font-weight: 400;
    letter-spacing: 0.5px;
    color: rgba(255, 255, 255, 0.92);
    line-height: 1;
  }
  .front-tagline {
    position: absolute;
    left: 82px;
    top: 155px;
    font-size: 16px;
    font-weight: 500;
    letter-spacing: 0.6px;
    color: rgba(255, 255, 255, 0.88);
    line-height: 1;
  }
  /* Contact side */
  .card-back {
    left: 602px;
    width: 481px;
    background: linear-gradient(180deg, var(--paper-light) 0%, var(--paper-dark) 100%);
  }
  .card-back .panel {
    position: absolute;
    inset: 0;
    width: 481px;
    height: 294px;
  }
  .brand-block {
    position: absolute;
    left: 0;
    width: 212px;
    top: 78px;
    text-align: center;
    color: var(--white);
  }
  .brand-dot {
    display: block;
    width: 56px;
    height: 56px;
    margin: 0 auto 22px;
    border: 4px solid var(--white);
    border-radius: 50%;
  }
  .brand-name {
    font-size: 17.5px;
    font-weight: 400;
    letter-spacing: 0.3px;
    line-height: 1;
  }
  .brand-tagline {
    margin-top: 6px;
    font-size: 8.8px;
    font-weight: 400;
    line-height: 1;
  }
  .person {
    position: absolute;
    left: 266px;
    top: 54px;
  }
  .person-name {
    font-family: "Exo 2", "Roboto", sans-serif;
    font-size: 21px;
    font-weight: 500;
    color: var(--teal);
    line-height: 1;
  }
  .person-title {
    margin-top: 6px;
    font-size: 13px;
    color: var(--ink);
    line-height: 1;
  }
  .contacts {
    position: absolute;
    left: 266px;
    top: 166px;
    list-style: none;
  }
  .contact {
    display: flex;
    align-items: center;
    height: 17.6px;
    font-size: 13px;
    color: var(--ink);
  }
  .contact-icon {
    width: 11px;
    height: 11px;
    margin-right: 10px;
    fill: var(--teal);
    flex: none;
  }
  .accent { color: var(--teal); }
</style>
</head>
<body>
<main class="canvas">

  <section class="card card-front" aria-label="Card front">
    <p class="front-name">QUORVANE CAPITAL</p>
    <p class="front-tagline">Diversified Crypto Investment Funds</p>
  </section>

  <section class="card card-back" aria-label="Card contact side">
    <svg class="panel" viewBox="0 0 481 294" aria-hidden="true">
      <defs>
        <linearGradient id="tealFill" x1="0" y1="0" x2="0" y2="1">
          <stop offset="0" stop-color="#188383"/>
          <stop offset="1" stop-color="#147474"/>
        </linearGradient>
      </defs>
      <path d="M200 0 C228 60 238 140 230 195 C222 245 212 272 200 294 H0 V0 Z" fill="#fcca46"/>
      <path d="M196 0 C224 60 232 140 222 190 C214 240 200 270 186 294 H0 V0 Z" fill="url(#tealFill)"/>
    </svg>

    <div class="brand-block">
      <span class="brand-dot"></span>
      <p class="brand-name">QUORVANE CAPITAL</p>
      <p class="brand-tagline">Diversified Crypto Investment Funds</p>
    </div>

    <div class="person">
      <p class="person-name">Daniel Okoro</p>
      <p class="person-title">Portfolio Engineer</p>
    </div>

    <ul class="contacts">
      <li class="contact">
        <svg class="contact-icon" viewBox="0 0 12 12" aria-hidden="true"><path d="M1 3.5 C1 2 3 1 6 1 C9 1 11 2 11 3.5 V4.5 H8.5 V3.5 H3.5 V4.5 H1 Z M2.5 5.5 H9.5 L10.5 11 H1.5 Z"/></svg>
        (303) 555-0192
      </li>
      <li class="contact">
        <svg class="contact-icon" viewBox="0 0 12 12" aria-hidden="true"><path d="M3 0.5 H9 V11.5 H3 Z M4 1.8 V9.5 H8 V1.8 Z"/></svg>
        +1 720 555 0147
      </li>
      <li class="contact">
        <svg class="contact-icon" viewBox="0 0 12 12" aria-hidden="true"><path d="M0.5 2.5 H11.5 V9.5 H0.5 Z M1.5 3.2 L6 6.6 L10.5 3.2 V3 H1.5 Z" fill-rule="evenodd"/></svg>
        daniel@quorvanecapital.example
      </li>
      <li class="contact">
        <svg class="contact-icon" viewBox="0 0 12 12" aria-hidden="true"><path d="M6 0.5 A5.5 5.5 0 1 0 6.01 0.5 Z M6 1.6 C7.2 2.8 7.6 4.4 7.7 5.5 H4.3 C4.4 4.4 4.8 2.8 6 1.6 Z M1.7 5.5 C1.9 3.8 3 2.4 4.5 1.9 C3.7 3 3.3 4.2 3.2 5.5 Z M8.8 5.5 C8.7 4.2 8.3 3 7.5 1.9 C9 2.4 10.1 3.8 10.3 5.5 Z M1.7 6.5 H3.2 C3.3 7.8 3.7 9 4.5 10.1 C3 9.6 1.9 8.2 1.7 6.5 Z M4.3 6.5 H7.7 C7.6 7.6 7.2 9.2 6 10.4 C4.8 9.2 4.4 7.6 4.3 6.5 Z M8.8 6.5 H10.3 C10.1 8.2 9 9.6 7.5 10.1 C8.3 9 8.7 7.8 8.8 6.5 Z" fill-rule="evenodd"/></svg>
        <span>www.<span class="accent">quorvanecapital</span>.example</span>
      </li>
    </ul>
  </section>

</main>
</body>
</html>
```